Looking for a modern website banner design

Bramblecrest Coaching Partners looking for the development of the main banner of the website. The project description and photos are included in the upload files.

```html
<!DOCTYPE html>
<html lang="en">
<head>
<meta charset="utf-8">
<title>Bramblecrest Coaching Partners – Testimonial Banner</title>
<link href="https://fonts.googleapis.com/css2?family=Raleway:ital,wght@0,400;0,500;0,700;1,400;1,500&display=swap" rel="stylesheet">
<style>
  :root {
    --ice-white: #f7fafc;
    --ice-pale: #e3eef5;
    --ice-blue: #b9d6e6;
    --ice-deep: #7fb0cc;
    --quote-mark: #c9d9ec;
    --text-dark: #2e3338;
    --ring-blue: #1f6fb8;
    --avatar-fill: #8aa5c4;
    --nav-grey: #55595d;
    --nav-icon: #ffffff;
  }
  * { box-sizing: border-box; margin: 0; padding: 0; }
  html, body { width: 1200px; height: 562px; overflow: hidden; background: var(--ice-white); }
  .banner {
    position: relative;
    width: 1200px;
    height: 562px;
    overflow: hidden;
    font-family: "Raleway", sans-serif;
    color: var(--text-dark);
  }
  .banner__scene {
    position: absolute;
    inset: 0;
    background:
      linear-gradient(90deg, var(--ice-white) 0%, rgba(247,250,252,0.95) 30%, rgba(247,250,252,0.4) 55%, rgba(247,250,252,0) 75%),
      linear-gradient(180deg, #cfe2ee 0%, #eef4f8 18%, var(--ice-blue) 45%, var(--ice-pale) 70%, var(--ice-deep) 100%);
  }
  .banner__quote-mark {
    position: absolute;
    left: 74px;
    top: 44px;
    width: 232px;
    height: 197px;
  }
  .testimonial__text {
    position: absolute;
    left: 244px;
    top: 52px;
    width: 410px;
    font-size: 21px;
    font-style: italic;
    font-weight: 500;
    line-height: 36.3px;
  }
  .testimonial__avatar {
    position: absolute;
    left: 245px;
    top: 333px;
    width: 184px;
    height: 184px;
    border-radius: 50%;
    border: 4px solid var(--ring-blue);
    background: radial-gradient(circle at 50% 45%, #e9eef5 0%, var(--avatar-fill) 55%, #3d4a5c 100%);
  }
  .testimonial__author {
    position: absolute;
    left: 454px;
    top: 368px;
    font-size: 19px;
    line-height: 35px;
  }
  .testimonial__name { font-weight: 700; }
  .testimonial__team, .testimonial__league { font-weight: 500; }
  .slider-nav {
    position: absolute;
    left: 892px;
    top: 487px;
    display: flex;
    gap: 13px;
  }
  .slider-nav__button {
    width: 26px;
    height: 26px;
    border-radius: 50%;
    background: var(--nav-grey);
    display: flex;
    align-items: center;
    justify-content: center;
  }
</style>
</head>
<body>
  <section class="banner">
    <div class="banner__scene" role="img" aria-label="Hockey player's skates, stick and puck on a frozen lake with snowy mountains behind"></div>

    <svg class="banner__quote-mark" viewBox="118 70 372 315" aria-hidden="true">
      <path fill="var(--quote-mark)" d="M118,345 L118,190 Q118,70 240,70 L260,70 L260,150 Q180,150 180,215 L250,215 Q290,215 290,255 L290,345 Q290,385 250,385 L158,385 Q118,385 118,345 Z"/>
      <path fill="var(--quote-mark)" d="M318,345 L318,190 Q318,70 440,70 L460,70 L460,150 Q380,150 380,215 L450,215 Q490,215 490,255 L490,345 Q490,385 450,385 L358,385 Q318,385 318,345 Z"/>
    </svg>

    <blockquote class="testimonial__text">
      “Bramblecrest has provided support that has allowed me to develop as a person and an athlete. The S.T.R.I.D.E.™ process allowed me to stay focused on attainable goals each season and progress from Junior to College and now Professional Hockey.”
    </blockquote>

    <div class="testimonial__avatar" role="img" aria-label="Portrait of the player in team jersey and helmet"></div>

    <div class="testimonial__author">
      <p class="testimonial__name">Marcus Trembly</p>
      <p class="testimonial__team">Riverton Falcons</p>
      <p class="testimonial__league">Northern Coast Hockey League</p>
    </div>

    <nav class="slider-nav" aria-label="Testimonial navigation">
      <span class="slider-nav__button" aria-label="Previous">
        <svg width="12" height="12" viewBox="0 0 12 12"><path d="M8 1.5 L3.5 6 L8 10.5" fill="none" stroke="var(--nav-icon)" stroke-width="2.4" stroke-linecap="round" stroke-linejoin="round"/></svg>
      </span>
      <span class="slider-nav__button" aria-label="Next">
        <svg width="12" height="12" viewBox="0 0 12 12"><path d="M4 1.5 L8.5 6 L4 10.5" fill="none" stroke="var(--nav-icon)" stroke-width="2.4" stroke-linecap="round" stroke-linejoin="round"/></svg>
      </span>
    </nav>
  </section>
</body>
</html>
```